International Property Consultancy

Brief Overview:

I need a dynamic and well designed website that is easy to use and understand. It has to be unique and different to generic templates that most websites seem to be these days. PLEASE NO GENERIC TEMPLATES FROM THE INTERNET.

Our business has 10 years experience working on struggling international developments that we then work in-house for to turn around and brings bout success. We stay within a project often for long periods of time until success is achieved. We are unique in our approach and completely different to the standard routes to market for many developments. The site is for developers to see what we have done in regards to previous projects, as such we want to incorporate video into this site with a strong design aesthetic. There will be videos of the past projects we have worked on, which will act as case studies.

I like very simple but punchy websites, that people can navigate and understand very easily. Also a big fan of unique and well thought out design aesthetic.

Initial Site layout thoughts:

1) Homepage:
2) About Us
3) What we've done / Work
This part has the projects we have worked on (France, Portugal, London, Morocco). Each one will have some video content and photo images, but also would be good to have a succinct way to mention what we did and the successes in a clever and punchy way.

4) Contact Us

* This is just a guideline. Would be open to input and creative direction on your own part.

*More details and websites we like can be seen in the brief doc attached.

PLEASE VIEW THE WIREFRAME WORD DOC ATTACHED.

Here there are also some more examples to help:

Here are just a few examples of websites and what I like about them:

- www.velmoro.com (clean, nice geometric design aesthetic, good animation when loading and changing pages well thought out all though also coulee be considered a bit dull and basic after the initial homepage slide)
- https://www.farbridgehub.net (Clean site, quite clinical, lacks video content and doesn't engage greatly).
- https://ruskotile.com (minimal, and like how it mixes the design aesthetic more with video and photo content)

- https://www.amberquillworks.com (like the layout of this and how it displays the projects and work section)

- https://brisk.com (Good use of video content)

- https://loomfield.studio (minimal to the point and mixes design with video and animation etc...)

Here is another couple of cool websites that may help give you some direction: https://halvenquay.com www.brisk.com

Hi there, One of the things I thought would be good on the homepage is to add the logo with a 'digital landscape' before flicking down into a slide with video content of the projects... Just an idea but have posted some pics in the brief. We would get this animated for the site. But if you have better ideas, please do run with them. Thanks,

Target Market(s)

Property developers

Number of Pages Required

4 page

Font styles to use
Other font styles liked:
• Read brief

Requirements
Must have
• Needs to be clean, dynamic and easy to follow on desktop and mobile. We will use it as a kind of portfolio website so will need to embed video of past projects we have worked on.

Read brief in docs.
Nice to have
• Clean
Should not have
• Not be another generic template website.
Not have random property stock photos. (We are not a property agency).

```html
<!DOCTYPE html>
<html lang="en">
<head>
<meta charset="utf-8">
<title>verandel — International Property Consultancy</title>
<link href="https://fonts.googleapis.com/css2?family=Baloo+2:wght@400;500;600;700&display=swap" rel="stylesheet">
<style>
:root{
  --ink:#111111;
  --text:#2a2a2a;
  --muted:#6b6b6b;
  --soft-bg:#fafafa;
  --line:#cfcfcf;
  --card-shade:rgba(60,60,60,.82);
  --white:#ffffff;
}
*{margin:0;padding:0;box-sizing:border-box}
html,body{width:842px;height:1200px;overflow:hidden;background:var(--white)}
body{font-family:'Baloo 2',sans-serif;color:var(--text);position:relative}
.abs{position:absolute}
.brand{font-weight:500;color:var(--ink);letter-spacing:-.3px;line-height:1}
.site-header .brand{left:43px;top:10px;font-size:22px}
.main-nav a{position:absolute;top:16px;font-size:7.5px;color:var(--text);text-decoration:none}
.main-nav a.active::after{content:"";position:absolute;left:50%;margin-left:-6px;bottom:-4px;width:12px;height:1.5px;background:var(--ink)}
.social-dot{position:absolute;width:9px;height:9px;border-radius:50%;background:var(--ink)}
.hero-visual{left:452px;top:45px;width:390px;height:350px;overflow:hidden}
.hero-visual .arc{position:absolute;left:0;top:0;width:560px;height:560px;border-radius:50%;background:linear-gradient(135deg,#f3f3f3,#fafafa)}
.hero-visual .photo{position:absolute;left:37px;top:0;width:520px;height:520px;border-radius:50%;background:linear-gradient(140deg,#f6f6f6 0%,#eeeeee 45%,#f8f8f8 100%)}
.play-btn{left:460px;top:188px;width:50px;height:50px;border-radius:50%;background:#f1f1f1}
.play-btn .core{position:absolute;left:5px;top:5px;width:40px;height:40px;border-radius:50%;background:var(--ink)}
.hero-intro{left:73px;top:160px;font-size:13.5px;color:var(--ink)}
.hero-title{left:73px;top:179px;font-size:19.5px;font-weight:700;color:var(--ink);white-space:nowrap}
.hero-body{left:73px;top:209px;font-size:9px;line-height:12.3px;color:var(--muted);width:270px}
.scroll-hint{left:43px;top:367px;font-size:8px;color:var(--muted)}
.about{left:0;top:395px;width:842px;height:253px;background:var(--soft-bg);text-align:center}
.section-title{font-size:13.5px;font-weight:600;color:var(--ink);letter-spacing:.3px;display:inline-block;position:relative}
.section-title::after{content:"";position:absolute;left:50%;margin-left:-7px;bottom:1px;width:14px;height:1.2px;background:var(--ink)}
.about .section-title{margin-top:48px}
.about-lead{font-size:12.8px;line-height:16.5px;color:var(--ink);margin-top:17px}
.about-body{font-size:8px;line-height:13px;color:var(--text);margin-top:14px}
.about-body b{color:var(--ink)}
.pill{display:inline-flex;align-items:center;gap:7px;border:.8px solid var(--line);border-radius:10px;font-size:7.5px;color:var(--ink);background:var(--white)}
.about .pill{margin-top:15px;padding:3px 13px}
.work-intro{left:127px;top:766px;width:150px}
.work-intro .section-title::after{left:33px;margin-left:0}
.work-text{font-size:7.8px;line-height:12.3px;color:var(--text);margin-top:14px}
.work-intro .pill{margin-top:13px;padding:3px 18px}
.project-card{top:700px;width:131px;height:219px;overflow:hidden}
.project-card .shade{position:absolute;left:0;right:0;bottom:0;height:56px;background:var(--card-shade)}
.project-card h3{position:absolute;left:12px;top:183px;font-size:9.5px;font-weight:600;color:var(--white);line-height:1}
.project-card span{position:absolute;left:12px;top:196px;font-size:6.6px;color:#e4e4e4}
.footer-bg{left:0;top:960px;width:842px;height:240px;background:linear-gradient(160deg,#ffffff 0%,#f6f6f6 50%,#ffffff 100%)}
.site-footer .brand{left:0;width:842px;text-align:center;top:992px;font-size:22px}
.tagline{left:0;width:842px;text-align:center;top:1021px;font-size:10px;color:var(--text)}
.contact-bar{left:151px;top:1065px;width:540px;height:57px;background:var(--white);box-shadow:0 2px 14px rgba(0,0,0,.04)}
.contact-item{position:absolute;font-size:7.3px;line-height:12px;color:var(--ink)}
.bar-divider{position:absolute;left:404px;top:15px;width:.8px;height:27px;background:#e6e6e6}
.footer-dot{position:absolute;top:26px;width:12px;height:12px;border-radius:50%;background:#6a6a6a}
.footer-nav{left:0;width:842px;top:1141px;text-align:center;font-size:7.5px;font-weight:500;color:var(--ink)}
.footer-nav span.sep{color:var(--muted);margin:0 14px;font-weight:400}
.copyright{left:0;width:842px;top:1160px;text-align:center;font-size:6.8px;color:var(--text)}
</style>
</head>
<body>

<header class="site-header">
  <div class="abs brand">verandel.</div>
  <nav class="main-nav">
    <a href="#" class="active" style="left:532px">Home</a>
    <a href="#" style="left:574px">About Us</a>
    <a href="#" style="left:627px">Work</a>
    <a href="#" style="left:667px">Contact Us</a>
  </nav>
  <span class="social-dot" style="left:755px;top:17px"></span>
  <span class="social-dot" style="left:774px;top:17px"></span>
  <span class="social-dot" style="left:793px;top:17px"></span>
</header>

<section class="hero">
  <div class="abs hero-visual">
    <div class="arc"></div>
    <div class="photo" role="img" aria-label="Faint white modern apartment building seen from below"></div>
  </div>
  <div class="abs play-btn">
    <div class="core">
      <svg width="40" height="40" viewBox="0 0 40 40"><path d="M15 11 L28 20 L15 29 Z" fill="none" stroke="#fff" stroke-width="2" stroke-linejoin="round"/></svg>
    </div>
  </div>
  <p class="abs hero-intro">Our business has</p>
  <h1 class="abs hero-title">10 years’ experience working</h1>
  <p class="abs hero-body">on struggling international developments that we then work in-house for to turn around and brings bout success.</p>
  <p class="abs scroll-hint">Scroll to explore
    <svg width="8" height="8" viewBox="0 0 8 8" style="vertical-align:-1px;margin-left:2px"><path d="M4 1v6M1.5 4.5L4 7l2.5-2.5" fill="none" stroke="#111" stroke-width="1"/></svg>
  </p>
</section>

<section class="abs about">
  <h2 class="section-title">ABOUT US</h2>
  <p class="about-lead">Verandel is a consultancy company that helps international property<br>developments fulfil their potential.</p>
  <p class="about-body">The company has had great success over the last <b>10 YEARS</b> of turning around struggling property developments (often resort and investment)<br>and making them reach their maximum potential. We have completed projects in Portugal, London, France, Morocco, Brazil etc...</p>
  <span class="pill">Read More
    <svg width="8" height="7" viewBox="0 0 8 7"><path d="M0 3.5h7M4.5 1L7 3.5 4.5 6" fill="none" stroke="#111" stroke-width="1"/></svg>
  </span>
</section>

<section class="work">
  <div class="abs work-intro">
    <h2 class="section-title">OUR WORK</h2>
    <p class="work-text">Lorem Ipsum is simply dummy text of the printing and typesetting industry. Lorem Ipsum has been the industry's standard dummy text ever...</p>
    <span class="pill">View All
      <svg width="8" height="7" viewBox="0 0 8 7"><path d="M0 3.5h7M4.5 1L7 3.5 4.5 6" fill="none" stroke="#111" stroke-width="1"/></svg>
    </span>
  </div>
  <article class="abs project-card" style="left:302px">
    <div role="img" aria-label="Grey and white modern building entrance" style="position:absolute;inset:0;background:linear-gradient(180deg,#9a9a9a 0%,#e8e8e8 30%,#cfcfcf 70%,#8c8c8c 100%)"></div>
    <div class="shade"></div><h3>Portugal Resort</h3><span>56 Propertys</span>
  </article>
  <article class="abs project-card" style="left:438px">
    <div role="img" aria-label="Bright interior with wooden staircase and pendant lights" style="position:absolute;inset:0;background:linear-gradient(180deg,#ececec 0%,#dcd6cf 45%,#b48a5c 80%,#6b5238 100%)"></div>
    <div class="shade"></div><h3>Morocco</h3><span>56 Propertys</span>
  </article>
  <article class="abs project-card" style="left:574px">
    <div role="img" aria-label="White stone building facade with dark windows" style="position:absolute;inset:0;background:linear-gradient(180deg,#4f5a55 0%,#e9e7e3 25%,#dedbd6 65%,#c9c5bf 100%)"></div>
    <div class="shade"></div><h3>London</h3><span>56 Propertys</span>
  </article>
  <article class="abs project-card" style="left:710px">
    <div role="img" aria-label="White villa with balconies under a pale blue sky" style="position:absolute;inset:0;background:linear-gradient(180deg,#cfe0e6 0%,#f1f1f0 35%,#e2dfdb 70%,#8d8a78 100%)"></div>
    <div class="shade"></div><h3>France</h3><span>56 Propertys</span>
  </article>
</section>

<footer class="site-footer">
  <div class="abs footer-bg" role="img" aria-label="Faint white architectural backdrop"></div>
  <div class="abs brand">verandel.</div>
  <p class="abs tagline">A special and qualified service dedicated to luxury properties</p>
  <div class="abs contact-bar">
    <svg style="position:absolute;left:45px;top:22px" width="11" height="13" viewBox="0 0 11 13"><path d="M5.5 12.3S1 7.6 1 5a4.5 4.5 0 0 1 9 0c0 2.6-4.5 7.3-4.5 7.3z" fill="none" stroke="#111" stroke-width=".9"/><circle cx="5.5" cy="5" r="1.6" fill="none" stroke="#111" stroke-width=".9"/></svg>
    <p class="contact-item" style="left:63px;top:16px">Lorem Ipsum, 47 Harbour Lane,<br>Sydney, Australia</p>
    <svg style="position:absolute;left:208px;top:16px" width="12" height="9" viewBox="0 0 12 9"><rect x=".5" y=".5" width="11" height="8" fill="none" stroke="#111" stroke-width=".9"/><path d="M.5.5l5.5 4.5L11.5.5M.5 8.5l4-3.5M11.5 8.5l-4-3.5" fill="none" stroke="#111" stroke-width=".9"/></svg>
    <p class="contact-item" style="left:180px;top:29px">info@verandel.com</p>
    <svg style="position:absolute;left:314px;top:15px" width="11" height="11" viewBox="0 0 11 11"><path d="M2.2 1l1.6 2.2-1 1.2a6 6 0 0 0 3.8 3.8l1.2-1L10 8.8 8.8 10C4.5 10 1 6.5 1 2.2z" fill="none" stroke="#111" stroke-width=".9"/><path d="M6.5 1.2a3.5 3.5 0 0 1 3.3 3.3M6.3 3a1.8 1.8 0 0 1 1.7 1.7" fill="none" stroke="#111" stroke-width=".8"/></svg>
    <p class="contact-item" style="left:293px;top:29px">+61 200 555 014</p>
    <span class="bar-divider"></span>
    <span class="footer-dot" style="left:427px"></span>
    <span class="footer-dot" style="left:452px"></span>
    <span class="footer-dot" style="left:476px"></span>
  </div>
  <nav class="abs footer-nav">Home<span class="sep">/</span>About Us<span class="sep">/</span>Work<span class="sep">/</span>Contact Us</nav>
  <p class="abs copyright">Copyright © 2020 verandel. All Rights Reserved</p>
</footer>

</body>
</html>
```